Recruitment technology firm needs a downloadable pdf to generate leads.

We need design work for a downloadable pdf that will serve as an educational document to visitors to our website. We help clients identify candidates that fit their job posting. We do that by defining the personality of the job and then assessing the personality of the candidates. We then mathematically compare and rank all the candidates against the job. Our colour scheme is blue. The final design should move from communicating a lack of fit or frustration to people fitting their job and success per the text we have built. People who download this lead generator will be added to our email list for re-marketing purposes. our website is www.tallowridgeadvisory.com. I've attached an example of a lead generator (ebike)for a business unrelated to ours.

Target Market(s)

Our target market is businesses of 50-300 people, we're targeting business owners or executives of entrepreneurial (vs. corporate) companies.

Colors
85acd3
3377b5
0455a3

Requirements
Must have
• Easy to read so text isn't overwhelming.
Nice to have
• Don't be compelled to use our website photos or those like it. I'd like this to reflect entrepreneurial companies, not corporate, suit and tie companies.

```html
<!DOCTYPE html>
<html lang="en">
<head>
<meta charset="utf-8">
<title>5 Reasons You Suck At Hiring For Fit – Tallowridge</title>
<link href="https://fonts.googleapis.com/css2?family=Plus+Jakarta+Sans:ital,wght@0,400;0,500;0,700;0,800;1,500&display=swap" rel="stylesheet">
<style>
  :root{
    --blue-light:#85acd3;
    --blue-mid:#3377b5;
    --blue-deep:#0455a3;
    --ink:#1b1b1b;
    --canvas:#e6e6e6;
    --paper:#ffffff;
    --cover-sky:#c4dbe6;
    --grid-grey:#d8d8d8;
    --job-red:#e0263c;
  }
  *{box-sizing:border-box;margin:0;padding:0}
  html,body{width:935px;height:1200px;overflow:hidden;background:var(--canvas)}
  body{font-family:"Plus Jakarta Sans",Arial,sans-serif;color:var(--ink);position:relative}
  .page{position:absolute;width:452px;height:585px;background:var(--paper);overflow:hidden}
  .page--cover{left:10px;top:10px;background:linear-gradient(180deg,#b8d3df 0%,var(--cover-sky) 60%,#cfe2ea 100%)}
  .page--one{left:473px;top:10px}
  .page--two{left:10px;top:606px}
  .page--three{left:473px;top:606px}

  .cover-photo{position:absolute;left:0;top:0;width:452px;height:410px;
    background:linear-gradient(160deg,#8c3f8e 0%,#f07a2a 22%,#7cc242 38%,#f2d42e 52%,#47b3d6 66%,#2a2a2a 80%,rgba(196,219,230,0) 100%)}
  .cover-brand{position:absolute;left:54px;top:426px;display:flex;align-items:center;gap:5px;
    font-weight:800;font-size:12.5px;letter-spacing:.4px;color:#4a4f55}
  .cover-brand .dot{width:11px;height:11px;border-radius:50%;background:var(--blue-deep)}
  .cover-title{position:absolute;left:54px;top:458px;font-size:28px;line-height:33px;font-weight:800;color:var(--blue-deep);letter-spacing:-.3px}

  .headline{position:absolute;left:37px;top:52px;font-size:16.5px;line-height:19.5px;font-weight:800;color:var(--blue-deep)}
  .subhead{position:absolute;left:37px;top:102px;font-size:16.5px;font-weight:800;color:var(--blue-light)}
  .rule{position:absolute;height:1px;width:45px;background:var(--blue-light)}
  .copy{position:absolute;font-size:8.6px;line-height:13px;color:var(--ink)}
  .copy p+p{margin-top:13px}
  .copy strong{font-weight:700}
  .reason h3{font-size:11.4px;line-height:14px;font-weight:800;color:var(--blue-deep);margin-bottom:2px}
  .reason h3.soft{color:var(--blue-light)}
  .section-title{position:absolute;font-size:16.5px;line-height:19.5px;font-weight:800;color:var(--blue-deep)}

  .footer{position:absolute;left:0;bottom:0;width:100%;height:32px;background:var(--blue-deep);color:#fff;
    font-size:7px;display:flex;align-items:center;padding-left:37px}
  .footer .item{display:flex;align-items:center;gap:4px;margin-right:14px}
  .footer .num{position:absolute;right:46px}

  .chart{position:absolute;left:58px;top:92px}
  .chart-intro{position:absolute;left:56px;top:58px;width:350px;font-size:9px;line-height:13px}

  .next{position:absolute;left:0;top:227px;width:452px;height:136px;background:linear-gradient(90deg,#3e83c2,var(--blue-deep));color:#fff}
  .next h2{position:absolute;top:31px;width:100%;text-align:center;font-size:17px;font-weight:800}
  .step{position:absolute;top:67px;width:140px;text-align:center;font-size:9px;line-height:13.5px;color:#e6f0fa}
  .step .badge{width:14px;height:14px;border-radius:50%;background:#fff;color:var(--blue-deep);font-size:9px;font-weight:800;
    line-height:14px;margin:0 auto 8px}
  .quote-mark{position:absolute;left:22px;top:360px;font-size:62px;font-weight:800;line-height:1;color:var(--blue-light)}
  .quote-title{position:absolute;left:68px;top:380px;font-size:11px;line-height:14px;font-style:italic;font-weight:500;color:var(--blue-mid)}
</style>
</head>
<body>

<section class="page page--cover">
  <div class="cover-photo" role="img" aria-label="Photo of colourful interlocking puzzle blocks each marked with a white person figure"></div>
  <div class="cover-brand"><span class="dot"></span>TALLOWRIDGE</div>
  <h1 class="cover-title">5 Reasons You Suck<br>At Hiring For Fit</h1>
</section>

<section class="page page--one">
  <h2 class="headline">Hiring the wrong fit is painful,<br>we are with you there.</h2>
  <p class="subhead">Bad hires ruin your day, every day.</p>
  <div class="rule" style="left:37px;top:132px"></div>
  <div class="copy" style="left:37px;top:148px;width:365px">
    <p>You want to make sure your next hire is the right one. You know what it’s like when you hire the wrong person – they aren’t productive, they don’t get along with others, there’s tension, you have to let them go, and you re-start the whole process over again.</p>
    <p><strong>Our goal is to help you stop this cycle. Here are 5 mistakes you are likely making.</strong></p>
  </div>
  <div class="copy reason" style="left:52px;top:246px;width:350px">
    <h3>1. You have not defined the obstacles found in the job.</h3>
    <p>Every job has its challenges and you need to find someone who will deal with the challenges as a high performer would. Spending too much time in unstructured conversation or putting too much emphasis on selling the role can detract from this key insight. Define the top 2-5 obstacles and learn how the candidate has or would tackle them</p>
  </div>
  <div class="copy reason" style="left:52px;top:342px;width:350px">
    <h3 class="soft">2. You describe the job using words, not data.</h3>
    <p>Every job has its challenges and you need to find someone who will deal with the challenges as a high performer would. Spending too much time in unstructured conversation or putting too much emphasis on selling the role can detract from this key insight. Define the top 2-5 obstacles and learn how the candidate has or would tackle them</p>
  </div>
  <div class="copy reason" style="left:52px;top:433px;width:352px">
    <h3>3. You assume knowledge and experience equals performance.</h3>
    <p>Just because someone’s resume says they are a strong manager does not mean they are one. And yet this is how you screen and rank your candidates. The best resumes rise to the top. But resumes are a terrible predictor of performance. Success at one company does not mean success in yours. Who are you overlooking that may be a better performer? (we have an idea below)</p>
  </div>
  <footer class="footer">
    <span class="item"><svg width="10" height="8" viewBox="0 0 10 8"><rect x=".5" y=".5" width="9" height="7" fill="none" stroke="#fff"/><path d="M.5 .5 5 4.5 9.5 .5" fill="none" stroke="#fff"/></svg>email@tallowridgeadvisory.com</span>
    <span class="item"><svg width="8" height="8" viewBox="0 0 8 8"><path d="M1 0h2l1 2-1.2 1a5 5 0 0 0 2.2 2.2L6 4l2 1v2a1 1 0 0 1-1 1A7 7 0 0 1 0 1a1 1 0 0 1 1-1z" fill="#fff"/></svg>855 555 0147</span>
    <span class="num">01</span>
  </footer>
</section>

<section class="page page--two">
  <div class="copy reason" style="left:55px;top:58px;width:350px">
    <h3 class="soft">4. You are biased and subjective in your assessment of others.</h3>
    <p>You get attracted to certain resumes and backgrounds. You make judgement calls on phone interviews. You do the same when you meet someone and during an interview. Very few recruitment processes have a way of OBJECTIVELY ranking and comparing candidates. As a result we end up picking someone we like as opposed to someone who will excel in the job.</p>
  </div>
  <div class="copy reason" style="left:55px;top:152px;width:350px">
    <h3>5. You think your “gut” makes good decisions.</h3>
    <p>“Gut” has more to do with how likeable someone is than how effective they will be. Effectiveness comes from a person’s ability to consistently behave in a manner that produces exceptional results. Do not make judgement calls on behaviours a candidate shows but may not be able to consistently repeat.</p>
  </div>
  <div class="rule" style="left:42px;top:252px"></div>
  <h2 class="section-title" style="left:43px;top:278px">So how can you<br>hire for fit?</h2>
  <div class="copy" style="left:43px;top:337px;width:180px;font-size:8.8px">
    <p>Personality is the most significant predictor of both fit to the manager and performance in the role. It is also one of the most difficult things to assess without the use of an objective tool.</p>
    <p>Most candidates behave a certain way in an interview, but it may be something that is difficult for them to sustain.</p>
    <p>To start addressing the problem of hiring bad fits you need to add more objectivity to your</p>
  </div>
  <div class="copy" style="left:234px;top:271px;width:175px;font-size:8.8px">
    <p>process. RoleGauge is a tool designed to define a benchmark of what personality is required in a role using data. Everyone gets on the same page of what success looks like.</p>
    <p>From there each candidate completes a Core.trait personality survey within the RoleGauge tool. Then they are compared equally to the benchmark and ranked objectively. All candidates are compared using the same personality dimensions.</p>
    <p>You leverage specific data and our insight to find the best candidates ... Your ability to consistently hire above average fits increases ... You achieve more.</p>
  </div>
  <footer class="footer" style="padding-left:36px">
    <span class="item"><svg width="10" height="8" viewBox="0 0 10 8"><rect x=".5" y=".5" width="9" height="7" fill="none" stroke="#fff"/><path d="M.5 .5 5 4.5 9.5 .5" fill="none" stroke="#fff"/></svg>email@tallowridgeadvisory.com</span>
    <span class="item"><svg width="8" height="8" viewBox="0 0 8 8"><path d="M1 0h2l1 2-1.2 1a5 5 0 0 0 2.2 2.2L6 4l2 1v2a1 1 0 0 1-1 1A7 7 0 0 1 0 1a1 1 0 0 1 1-1z" fill="#fff"/></svg>855 555 0147</span>
    <span class="num">02</span>
  </footer>
</section>

<section class="page page--three">
  <p class="chart-intro">Here are the results of a candidate compared to a job. The job is represented in red, the candidate is represented in black.</p>
  <div class="next">
    <h2>What’s next?</h2>
    <div class="step" style="left:6px"><div class="badge">1</div>Contact us to discuss<br>your position</div>
    <div class="step" style="left:155px"><div class="badge">2</div>Leverage our tools, process and<br>insights throughout your process</div>
    <div class="step" style="left:300px"><div class="badge">3</div>Welcome a great new team<br>member and crush your goals</div>
  </div>
  <svg class="chart" width="336" height="148" viewBox="0 0 336 148" font-family="Plus Jakarta Sans, Arial, sans-serif">
    <rect x="0" y="0" width="336" height="148" fill="#fff"/>
    <rect x="0" y="0" width="51" height="66" fill="var(--blue-mid)"/>
    <rect x="0" y="82" width="51" height="49" fill="var(--blue-mid)"/>
    <rect x="0" y="66" width="336" height="16" fill="var(--grid-grey)"/>
    <rect x="0" y="131" width="336" height="17" fill="var(--grid-grey)"/>
    <g stroke="var(--blue-mid)" stroke-width=".6">
      <line x1="0" y1="0.3" x2="336" y2="0.3"/><line x1="0" y1="16.5" x2="336" y2="16.5"/>
      <line x1="0" y1="33" x2="336" y2="33"/><line x1="0" y1="49.5" x2="336" y2="49.5"/>
      <line x1="0" y1="98" x2="336" y2="98"/><line x1="0" y1="114.5" x2="336" y2="114.5"/>
    </g>
    <line x1="193" y1="0" x2="193" y2="66" stroke="#5aaee0" stroke-width=".6" stroke-dasharray="2 2"/>
    <g fill="#fff" font-size="4.3">
      <text x="2" y="10">ASSERTIVENESS</text><text x="2" y="26.5">SOCIALBILITY</text>
      <text x="2" y="43">PACE</text><text x="2" y="59.5">DETAIL ORIENTATION</text>
      <text x="2" y="88">BEHAVIORAL</text><text x="2" y="93.5">ADAPTABILITY</text>
      <text x="2" y="108">EMOTIVENESS</text><text x="2" y="124.5">CREATIVITY</text>
    </g>
    <g fill="#333" font-size="4.5" text-anchor="middle">
      <text x="65" y="76">-5</text><text x="91" y="76">-4</text><text x="116" y="76">-3</text><text x="142" y="76">-2</text><text x="167" y="76">-1</text>
      <text x="193" y="76">0</text><text x="219" y="76">1</text><text x="244" y="76">2</text><text x="270" y="76">3</text><text x="295" y="76">4</text><text x="321" y="76">5</text>
      <text x="65.5" y="141">0</text><text x="91" y="141">1</text><text x="117" y="141">2</text><text x="143" y="141">3</text><text x="169" y="141">4</text>
      <text x="195" y="141">5</text><text x="220" y="141">6</text><text x="246" y="141">7</text><text x="272" y="141">8</text><text x="298" y="141">9</text><text x="324" y="141">10</text>
    </g>
    <polyline points="228,6.5 212,24.5 143,41 182,57.5" fill="none" stroke="var(--job-red)" stroke-width=".6" stroke-dasharray="1.5 1.5"/>
    <polyline points="237,6.5 180,24.5 168,41 189,57.5" fill="none" stroke="#111" stroke-width=".7"/>
    <g fill="var(--job-red)">
      <rect x="225.5" y="4" width="5" height="5"/><rect x="209.5" y="22" width="5" height="5"/>
      <rect x="140.5" y="38.5" width="5" height="5"/><rect x="179.5" y="55" width="5" height="5"/>
      <rect x="215.5" y="87.5" width="5" height="5"/><rect x="215.5" y="103.5" width="5" height="5"/><rect x="215.5" y="120.5" width="5" height="5"/>
    </g>
    <g fill="#111">
      <circle cx="237" cy="6.5" r="2.5"/><circle cx="180" cy="24.5" r="2.5"/><circle cx="168" cy="41" r="2.5"/><circle cx="189" cy="57.5" r="2.5"/>
      <circle cx="261" cy="90" r="2.5"/><circle cx="298" cy="106" r="2.5"/><circle cx="227" cy="123" r="2.5"/>
    </g>
  </svg>
  <div class="quote-mark">“</div>
  <p class="quote-title">What RoleGauge users<br>are saying...</p>
  <div class="copy" style="left:37px;top:423px;width:185px;font-size:8.8px">
    <p>The process changes we have made in recruiting as a result of working with Tallowridge’s RoleGauge have been transformational. We went into the interviews with confidence which ultimately made it easier to select the right candidate for the roles. Thanks to your tools and assessments I have a stronger team!<br>VP, Oil &amp; Gas Sector</p>
  </div>
  <div class="copy" style="left:233px;top:375px;width:195px;font-size:8.8px">
    <p>We’ve had very good success over the past year and a half since I’ve been in this role with reducing our turnover from around 50% to less than 10%. I feel very strongly that much of that has to do with our practice of only hiring people who are a match for our benchmarks.<br>Recruiter, IT Sector</p>
    <p>RoleGauge allows us to identify those that don’t fit our benchmark early so we don’t spend time with those that don’t fit.<br>Owner, Auto Industry</p>
  </div>
  <footer class="footer">
    <span class="item"><svg width="10" height="8" viewBox="0 0 10 8"><rect x=".5" y=".5" width="9" height="7" fill="none" stroke="#fff"/><path d="M.5 .5 5 4.5 9.5 .5" fill="none" stroke="#fff"/></svg>email@tallowridgeadvisory.com</span>
    <span class="item"><svg width="8" height="8" viewBox="0 0 8 8"><path d="M1 0h2l1 2-1.2 1a5 5 0 0 0 2.2 2.2L6 4l2 1v2a1 1 0 0 1-1 1A7 7 0 0 1 0 1a1 1 0 0 1 1-1z" fill="#fff"/></svg>855 555 0147</span>
    <span class="num" style="right:44px">03</span>
  </footer>
</section>

</body>
</html>
```